Atendimento nota 11, sem contar a agilidade das pessoas, nos apresentaram diversos modelos e formas de logo. Com certeza iremos indica-lo para outras pessoas.

```html
<!DOCTYPE html>
<html lang="pt-BR">
<head>
<meta charset="UTF-8">
<title>Verane Imóveis — Cartão de visita</title>
<link href="https://fonts.googleapis.com/css2?family=Josefin+Sans:wght@300&family=Montserrat:wght@400&family=Arimo:wght@400&display=swap" rel="stylesheet">
<style>
  :root {
    --backdrop: #e9e9e7;
    --brown: #2f1f13;
    --gold: #c9ab72;
    --white: #ffffff;
    --ink: #3a3a3a;
    --ink-soft: #555555;
    --faint: #f3f3f3;
  }
  * { margin: 0; padding: 0; box-sizing: border-box; }
  html, body { width: 1200px; height: 1200px; overflow: hidden; }
  body { background: var(--backdrop); position: relative; }

  .card {
    position: absolute;
    left: 240px;
    width: 720px;
    box-shadow: 0 4px 14px rgba(0,0,0,0.18);
    overflow: hidden;
  }

  /* Front */
  .card-front { top: 180px; height: 396px; background: var(--brown); }
  .brand-front {
    position: absolute; left: 0; right: 0; top: 150px;
    display: flex; flex-direction: column; align-items: center;
    color: var(--gold);
    font-family: "Josefin Sans", sans-serif; font-weight: 300;
  }
  .brand-front .mark {
    width: 26px; height: 26px; background: var(--gold); margin-bottom: 22px;
  }
  .brand-front .name { font-size: 60px; letter-spacing: 4px; line-height: 1; }
  .brand-front .sub { font-size: 22px; letter-spacing: 16px; margin-top: 12px; padding-left: 16px; }
  .front-rule {
    position: absolute; left: 0; right: 0; top: 340px; height: 3px; background: var(--gold);
  }

  /* Back */
  .card-back { top: 612px; height: 408px; background: var(--white); }
  .faint-name {
    position: absolute; right: -30px; top: 30px;
    font-family: "Josefin Sans", sans-serif; font-weight: 300;
    font-size: 190px; line-height: 1; color: var(--faint);
  }
  .brand-back {
    position: absolute; left: 90px; top: 160px;
    display: flex; align-items: center; gap: 14px;
    color: var(--gold);
    font-family: "Josefin Sans", sans-serif; font-weight: 300;
    font-size: 40px; letter-spacing: 3px;
  }
  .brand-back .mark { width: 22px; height: 22px; background: var(--gold); }

  .person {
    position: absolute; right: 86px; top: 98px; text-align: right;
    font-family: "Montserrat", sans-serif; color: var(--ink);
  }
  .person .full-name { font-size: 21px; letter-spacing: 1.5px; }
  .person .role { font-size: 15px; letter-spacing: 1px; margin-top: 12px; color: var(--ink-soft); }

  .contacts {
    position: absolute; right: 80px; top: 210px; list-style: none;
    font-family: "Arimo", sans-serif; font-size: 13.5px; color: var(--ink-soft);
  }
  .contacts li {
    display: flex; align-items: center; justify-content: flex-end; gap: 14px;
    height: 32px;
  }
  .contacts svg { width: 18px; height: 18px; display: block; }

  .back-rule {
    position: absolute; left: 0; right: 0; top: 362px; height: 3px; background: var(--brown);
  }
</style>
</head>
<body>
  <section class="card card-front">
    <div class="brand-front">
      <span class="mark"></span>
      <span class="name">VERANE</span>
      <span class="sub">IMÓVEIS</span>
    </div>
    <div class="front-rule"></div>
  </section>

  <section class="card card-back">
    <div class="faint-name" aria-hidden="true">VERANE</div>
    <div class="brand-back"><span class="mark"></span>VERANE</div>

    <div class="person">
      <p class="full-name">RAFAEL SOUZA MARTINS</p>
      <p class="role">AGENCIADOR</p>
    </div>

    <ul class="contacts">
      <li>Rua 140, nº 85, Sala 04 - Porto Belo - Centro - SC
        <svg viewBox="0 0 18 18"><rect width="18" height="18" rx="2" fill="#2f1f13"/><path d="M9 3.5a3.3 3.3 0 0 0-3.3 3.3c0 2.5 3.3 6.7 3.3 6.7s3.3-4.2 3.3-6.7A3.3 3.3 0 0 0 9 3.5z" fill="#fff"/><circle cx="9" cy="6.8" r="1.2" fill="#2f1f13"/></svg>
      </li>
      <li>(47) 3300-0000 - (47) 9000-0000
        <svg viewBox="0 0 18 18"><rect width="18" height="18" rx="2" fill="#2f1f13"/><path d="M5.2 4.2l2 0.1 0.9 2.3-1.2 0.9c0.6 1.3 1.5 2.2 2.8 2.8l0.9-1.2 2.3 0.9 0.1 2c-0.3 0.7-1 1-1.8 0.9-3.6-0.5-6.3-3.2-6.8-6.8-0.1-0.8 0.2-1.5 0.8-1.9z" fill="#fff"/></svg>
      </li>
      <li>rafael@veraneimoveis.com.br
        <svg viewBox="0 0 18 18"><rect width="18" height="18" rx="2" fill="#2f1f13"/><rect x="4" y="5.5" width="10" height="7" fill="#fff"/><path d="M4 5.5l5 4 5-4" stroke="#2f1f13" stroke-width="1" fill="none"/></svg>
      </li>
      <li>www.veraneimoveis.com.br
        <svg viewBox="0 0 18 18"><rect width="18" height="18" rx="2" fill="#2f1f13"/><circle cx="9" cy="9" r="4.5" stroke="#fff" stroke-width="1.2" fill="none"/><path d="M4.5 9h9M9 4.5c-2 2.5-2 6.5 0 9M9 4.5c2 2.5 2 6.5 0 9" stroke="#fff" stroke-width="1" fill="none"/></svg>
      </li>
    </ul>

    <div class="back-rule"></div>
  </section>
</body>
</html>
```